Real Estate Business Cards

Looking for a clean, sharp and professional look for our Real Estate investment Fund that invests in Multi Family Apartment buildings.

Target Market(s)

Real Estate Fund

Industry/Entity Type

Real Estate

Contact Information for Business Card

Company Description: Real Estate Investment Fund
Company Name: RKW Holdings
Name: Marcus Olvane
Cell: (917) 482-0657
Email: marcus@rkwholdings-example.com
Website: www.rkwholdings-example.com
Address: 418, 9th Street, Brooklyn NY 11218

Colors

Designer to choose colors to be used in the design.

Requirements
Nice to have
• Colors to match logo

```html
<!DOCTYPE html>
<html lang="en">
<head>
<meta charset="utf-8">
<title>RKW Holdings — Business Card</title>
<link href="https://fonts.googleapis.com/css2?family=Poppins:wght@400;600&family=Cormorant+Garamond:wght@500&display=swap" rel="stylesheet">
<style>
  :root {
    --backdrop: #ebebeb;
    --card: #f7f7f7;
    --ink: #3a3a3a;
    --muted: #555555;
    --brand-blue: #4a7bb7;
    --rule: #8fa9cc;
  }
  * { box-sizing: border-box; margin: 0; padding: 0; }
  html, body { width: 1200px; height: 800px; overflow: hidden; }
  body {
    background: var(--backdrop);
    display: flex;
    align-items: center;
    justify-content: center;
    gap: 60px;
    font-family: "Poppins", sans-serif;
  }
  .card {
    width: 520px;
    height: 297px;
    background: var(--card);
    box-shadow: 0 10px 30px rgba(0,0,0,0.12);
    display: flex;
    align-items: center;
    justify-content: center;
  }
  /* Front */
  .front-layout {
    display: flex;
    align-items: flex-end;
    gap: 18px;
  }
  .brand-mark {
    display: flex;
    flex-direction: column;
    align-items: center;
    gap: 8px;
  }
  .brand-square {
    width: 46px;
    height: 46px;
    background: var(--brand-blue);
  }
  .brand-name {
    font-family: "Cormorant Garamond", serif;
    font-weight: 500;
    font-size: 13px;
    letter-spacing: 1.5px;
    text-transform: uppercase;
    color: var(--brand-blue);
    white-space: nowrap;
  }
  .details { display: flex; flex-direction: column; }
  .person-name {
    font-weight: 600;
    font-size: 22px;
    color: var(--ink);
    margin-bottom: 6px;
    line-height: 1.1;
    white-space: nowrap;
  }
  .contact-block {
    display: flex;
    align-items: stretch;
    gap: 12px;
  }
  .divider {
    width: 1px;
    background: var(--rule);
    flex: none;
  }
  .contact-list { list-style: none; }
  .contact-item {
    display: flex;
    align-items: center;
    gap: 7px;
    font-size: 8px;
    letter-spacing: 1px;
    color: var(--muted);
    line-height: 15px;
    white-space: nowrap;
  }
  .contact-icon { width: 8px; height: 8px; flex: none; }
  .contact-icon * { fill: none; stroke: var(--brand-blue); stroke-width: 2; }
  .contact-icon .solid { fill: var(--brand-blue); stroke: none; }
  /* Back */
  .back .wordmark { display: flex; align-items: center; gap: 12px; }
  .back .brand-square { width: 38px; height: 38px; }
  .back .brand-name { font-size: 26px; letter-spacing: 2px; }
</style>
</head>
<body>
  <section class="card front" aria-label="Card front">
    <div class="front-layout">
      <div class="brand-mark">
        <div class="brand-square"></div>
        <span class="brand-name">RKW Holdings</span>
      </div>
      <div class="details">
        <h1 class="person-name">Marcus Olvane</h1>
        <div class="contact-block">
          <div class="divider"></div>
          <ul class="contact-list">
            <li class="contact-item">
              <svg class="contact-icon" viewBox="0 0 10 10"><path class="solid" d="M2 0.5 L3.6 2.6 L2.8 3.6 Q4 6 6.4 7.2 L7.4 6.4 L9.5 8 L8.5 9.5 Q3.5 9 0.5 1.5 Z"/></svg>
              (917) 482-0657
            </li>
            <li class="contact-item">
              <svg class="contact-icon" viewBox="0 0 10 10"><rect x="1" y="2" width="8" height="6"/><path d="M1 2 L5 5.5 L9 2"/></svg>
              marcus@rkwholdings-example.com
            </li>
            <li class="contact-item">
              <svg class="contact-icon" viewBox="0 0 10 10"><circle cx="5" cy="5" r="4"/><path d="M1 5 H9 M5 1 Q2.5 5 5 9 M5 1 Q7.5 5 5 9"/></svg>
              www.rkwholdings-example.com
            </li>
            <li class="contact-item">
              <svg class="contact-icon" viewBox="0 0 10 10"><path class="solid" d="M5 0.5 A3.5 3.5 0 0 1 8.5 4 Q8.5 6.5 5 9.5 Q1.5 6.5 1.5 4 A3.5 3.5 0 0 1 5 0.5 Z M5 2.6 A1.4 1.4 0 1 0 5 5.4 A1.4 1.4 0 1 0 5 2.6 Z"/></svg>
              418, 9th Street, Brooklyn NY 11218
            </li>
          </ul>
        </div>
      </div>
    </div>
  </section>

  <section class="card back" aria-label="Card back">
    <div class="wordmark">
      <div class="brand-square"></div>
      <span class="brand-name">RKW Holdings</span>
    </div>
  </section>
</body>
</html>
```